依頼詳細
専門ひだまり便もスタートしたので、名刺を新しく作り直そうと思っております。
ひだまり便事業部の中に【家族ひだまり便】と【専門ひだまり便】というターゲットが違う仕事をしているだけで、対応するメンバーは、変わらないので、名刺を一枚にまとめたいと考えています。
両方のチラシを添付しておりますし、ホームページもあります。
全員で7名分作成のお願いが出来たらと思います。
記載項目は入れたいと思っております。それ以外は、お任せいたします。

宜しくお願いいたします。
記載項目
表面:会社名、住所、093-555-0142、FAX、info@hidamari-bin.example、個人の資格、名前と役職、似顔絵
裏面:家族ひだまり便の事業内容・不用品回収、遺品整理、生前整理、住まいのお困り事対応サービス
専門ひだまり便の事業内容・弁護士、司法書士、税理士などの士業専門の不用品回収や遺品整理、機密文書処理
会社の資格:北九州市一廃廃棄物収集運搬許可 北九一廃第382号
希望イメージ
シンプル 複雑
単色 カラフル
暗い 明るい
日常 高級
遊び心 厳粛
未来的 伝統的
女性的 男性的
希望する色
緑系、青系、水色系
納品ファイル
• 高解像度JPG (.jpg)
• イラストレーター形式 (.ai)
• PNG形式 (.png)
補足説明
会社の許可の部分で、あと2つ許可を追加していただけたらと思います。
産業廃棄物処分業許可 第05213384720号
産業廃棄物収集運搬業 06281937402
上記2点です。
宜しくお願いいたします。
■ 選んだ理由

シンプルかつ私がイメージしていた名刺のデザインだったため、選ばせていただきました。

■ 提案者全員のお礼・コメント

色々と提案していただき、ありがとうございました。
どれにするかとても迷うぐらい良い物ばかりでした。
今後とも宜しくお願いいたします。

```html
<!DOCTYPE html>
<html lang="ja">
<head>
<meta charset="utf-8">
<title>ひだまり便 名刺</title>
<link href="https://fonts.googleapis.com/css2?family=Noto+Sans+JP:wght@400;500;700;900&display=swap" rel="stylesheet">
<style>
:root{
  --paper:#ffffff;
  --bg:#ffffff;
  --crop:#9a9a9a;
  --ink:#222222;
  --blue:#1f6fc2;
  --teal:#23a7b8;
  --teal-dark:#16808f;
  --red:#e0322b;
  --yellow:#ffe23a;
  --green:#3aa55a;
  --sky:#1a9ad6;
  --figure-a:#e9c9a8;
  --figure-b:#7fb8e0;
}
*{margin:0;padding:0;box-sizing:border-box}
html,body{width:846px;height:1200px;overflow:hidden;background:var(--bg)}
body{position:relative;font-family:"Noto Sans JP",sans-serif;color:var(--ink)}
.crop-marks{position:absolute;left:0;top:0}
.card{position:absolute;left:197px;width:470px;height:284px;background:var(--paper)}
.card--front{top:127px}
.card--back{top:600px}

.headline{position:absolute;left:12px;top:12px;font-size:15px;font-weight:900;color:var(--blue);white-space:nowrap;line-height:20px}
.headline em{font-style:normal;color:var(--red)}
.portrait-panel{position:absolute;right:8px;top:40px;width:150px;height:186px;
  background:linear-gradient(160deg,#5cc7d4,var(--teal) 55%,var(--teal-dark));}
.bubble{position:absolute;right:14px;top:178px;width:138px;background:var(--red);color:var(--yellow);
  font-size:12px;font-weight:900;line-height:16px;padding:4px 6px;border-radius:10px;text-align:center}

.qualification{position:absolute;left:84px;top:86px;font-size:8px;line-height:12px}
.person{position:absolute;left:62px;top:100px;display:flex;align-items:baseline;gap:12px}
.person .role{font-size:10px;font-weight:500}
.person .name{font-size:24px;font-weight:700;letter-spacing:3px;line-height:32px}
.company{position:absolute;left:14px;top:148px;font-size:16px;font-weight:700;line-height:22px}
.contacts{position:absolute;left:16px;top:176px;list-style:none;font-size:9px;line-height:15px}
.contacts li{display:flex;align-items:center;gap:6px;white-space:nowrap}
.contacts svg{flex:none}

.service{position:absolute;top:56px;width:170px;text-align:center}
.service--family{left:56px}
.service--pro{left:234px}
.service-name{display:flex;align-items:center;justify-content:center;gap:6px;
  font-size:15px;font-weight:700;height:64px}
.service--family .service-name{color:var(--green)}
.service--pro .service-name{color:var(--sky)}
.mark-circle{width:14px;height:14px;border-radius:50%;background:var(--green)}
.mark-square{width:14px;height:14px;background:var(--sky)}
.service-detail{margin-top:6px;font-size:8px;line-height:12px}
.permits{position:absolute;left:80px;top:196px;display:flex;gap:14px;font-size:8px;line-height:12px}
.permits .label{padding-top:12px}

.figures{position:absolute;left:16px;top:960px;width:814px;height:172px;display:flex;justify-content:space-between}
.figure{width:118px;height:172px;border-radius:40px 40px 8px 8px;
  background:linear-gradient(180deg,var(--figure-a) 0 45%,var(--figure-b) 45% 100%)}
</style>
</head>
<body>

<svg class="crop-marks" width="846" height="940" viewBox="0 0 846 940" aria-hidden="true">
  <g stroke="var(--crop)" stroke-width="1" fill="none">
    <path d="M157 127H189M197 87V119M157 411H189M197 419V451M707 127H675M667 87V119M707 411H675M667 419V451M150 269H178M432 97V119M432 419V441"/>
    <path d="M157 600H189M197 560V592M157 884H189M197 892V924M707 600H675M667 560V592M707 884H675M667 892V924M150 742H178M432 570V592M432 892V914"/>
  </g>
</svg>

<section class="card card--front">
  <p class="headline">北九州市から<em>許可</em>をもらって営業しているプロ集団です!</p>
  <div class="portrait-panel" role="img" aria-label="担当者の似顔絵イラスト、水色の格子背景"></div>
  <p class="bubble">不用品回収なら<br>お任せ!</p>

  <p class="qualification">遺品整理士資格保有</p>
  <div class="person"><span class="role">担当</span><span class="name">日向 健太</span></div>
  <p class="company">株式会社ヒナタ</p>
  <ul class="contacts">
    <li><svg width="10" height="10" viewBox="0 0 12 12"><circle cx="6" cy="6" r="6" fill="var(--green)"/><path d="M6 2.5a2 2 0 0 0-2 2c0 1.6 2 4 2 4s2-2.4 2-4a2 2 0 0 0-2-2z" fill="#fff"/></svg>〒803-0000 北九州市小倉北区陽だまり町1-2-3</li>
    <li><svg width="10" height="10" viewBox="0 0 12 12"><circle cx="6" cy="6" r="6" fill="var(--green)"/><path d="M4 3l1 .3.4 1.5-.7.6a4 4 0 0 0 1.9 1.9l.6-.7 1.5.4L9 8c-2.5.6-5.6-2.5-5-5z" fill="#fff"/></svg>TEL 093-555-0142</li>
    <li><svg width="10" height="10" viewBox="0 0 12 12"><circle cx="6" cy="6" r="6" fill="var(--green)"/><rect x="3" y="4" width="6" height="4.5" fill="#fff"/></svg>FAX 093-555-0143</li>
    <li><svg width="10" height="10" viewBox="0 0 12 12"><circle cx="6" cy="6" r="6" fill="var(--green)"/><path d="M3 4h6v4H3z" fill="#fff"/><path d="M3 4l3 2.2L9 4" stroke="var(--green)" stroke-width=".8" fill="none"/></svg>info@hidamari-bin.example</li>
    <li><svg width="10" height="10" viewBox="0 0 12 12"><circle cx="6" cy="6" r="6" fill="var(--green)"/><circle cx="6" cy="6" r="3" stroke="#fff" fill="none"/></svg>www.hidamari-bin.example</li>
  </ul>
</section>

<section class="card card--back">
  <div class="service service--family">
    <p class="service-name"><span class="mark-circle"></span>家族ひだまり便</p>
    <p class="service-detail">不用品回収・遺品整理・生前整理<br>住まいのお困り事対応サービス</p>
  </div>
  <div class="service service--pro">
    <p class="service-name"><span class="mark-square"></span>専門ひだまり便</p>
    <p class="service-detail">弁護士・司法書士・税理士など<br>士業専門の不用品回収・遺品整理<br>機密文書処理</p>
  </div>
  <div class="permits">
    <p class="label">会社の許可</p>
    <p>北九州市一般廃棄物収集運搬許可 北九一廃第382号<br>産業廃棄物処分業許可 第05213384720号<br>産業廃棄物収集運搬業 06281937402</p>
  </div>
</section>

<div class="figures">
  <div class="figure" role="img" aria-label="スタッフ似顔絵イラスト1"></div>
  <div class="figure" role="img" aria-label="スタッフ似顔絵イラスト2"></div>
  <div class="figure" role="img" aria-label="スタッフ似顔絵イラスト3"></div>
  <div class="figure" role="img" aria-label="スタッフ似顔絵イラスト4"></div>
  <div class="figure" role="img" aria-label="スタッフ似顔絵イラスト5"></div>
  <div class="figure" role="img" aria-label="スタッフ似顔絵イラスト6"></div>
</div>

</body>
</html>
```